High Tech Real Estate Startup needs a business card

We are developing an innovative real estate marketing product based around advanced search and virtual reality.

We talk to people, we need business cards.

Target Market(s)

The target market is technology professionals and realtors.

Contact Information for Business Card

The information to be included will include

Name
Title
Phone Number
E-mail Address
www.plindo.com

It should use simple iconography for each one of those fields.

Font styles to use
Other font styles liked:
• Co, Jubilat, Avenir

Colors

Designer to choose colors to be used in the design.

Requirements
Must have
• Clean aesthetic,
• Good use of negative space.
• It should use our company logo, shown in the attached file. It is able to use the negative of that logo (coloured font and white background) and I have attached other acceptable accent colours in a swatch file.
Should not have
• Should not be too busy
• No extraneous text (slogans, tag lines etc)

```html
<!DOCTYPE html>
<html lang="en">
<head>
<meta charset="utf-8">
<title>Plindo Business Card</title>
<link rel="stylesheet" href="https://fonts.googleapis.com/css2?family=Montserrat:wght@500&family=Roboto+Condensed:wght@300;400;700&display=swap">
<style>
  :root {
    --teal: #00b9c0;
    --white: #ffffff;
    --rule: rgba(255, 255, 255, 0.55);
    --page: #e9ecec;
  }
  * { margin: 0; padding: 0; box-sizing: border-box; }
  html, body {
    width: 1200px;
    height: 911px;
    overflow: hidden;
    background: var(--page);
  }
  .sheet {
    width: 1200px;
    height: 911px;
    display: flex;
    align-items: center;
    justify-content: center;
    gap: 40px;
  }
  .card {
    position: relative;
    width: 560px;
    height: 320px;
    background: var(--teal);
    color: var(--white);
    box-shadow: 0 6px 18px rgba(0, 0, 0, 0.18);
  }
  .wordmark {
    font-family: "Montserrat", sans-serif;
    font-weight: 500;
    letter-spacing: 3px;
    line-height: 1;
  }
  .card-front .wordmark {
    position: absolute;
    top: 44px;
    left: 0;
    width: 100%;
    text-align: center;
    font-size: 52px;
  }
  .card-front .identity {
    position: absolute;
    left: 30px;
    bottom: 62px;
    font-family: "Roboto Condensed", sans-serif;
    font-size: 20px;
    letter-spacing: 0.3px;
  }
  .identity .name { font-weight: 700; }
  .identity .title { font-weight: 300; font-size: 15px; }
  .card-front .rule {
    position: absolute;
    left: 30px;
    right: 30px;
    bottom: 50px;
    height: 1px;
    background: var(--rule);
  }
  .card-front .contact {
    position: absolute;
    left: 30px;
    bottom: 26px;
    font-family: "Roboto Condensed", sans-serif;
    font-weight: 300;
    font-size: 14px;
    letter-spacing: 0.3px;
    display: flex;
    gap: 10px;
  }
  .card-back {
    display: flex;
    align-items: center;
    justify-content: center;
  }
  .card-back .wordmark { font-size: 76px; }
</style>
</head>
<body>
  <main class="sheet">
    <section class="card card-front">
      <div class="wordmark">PLINDO</div>
      <div class="identity"><span class="name">DANIEL REYES</span> <span class="title">- CEO/FOUNDER</span></div>
      <div class="rule"></div>
      <div class="contact">
        <span>P. 555 210 4817</span>
        <span>E. daniel@plindo.com</span>
        <span>W. www.plindo.com</span>
      </div>
    </section>
    <section class="card card-back">
      <div class="wordmark">PLINDO</div>
    </section>
  </main>
</body>
</html>
```